Vodka bottle label for premium caribbean market

Label design for a Vodka bottle
Vodka name is 742 Vodka
General colors desired are red and blue
This is a premium vodka product that will be made and distributed in the Caribbean
The art in the background are used in religious celebrations and need to be incorporated
The 742 Vodka design is what I personally created and want to follow a similar art design
Logo should say 742 Vodka

Reason: I was out on leave for personal reasons but ready to make a decision as soon as possible.

Target Market(s)

Premium vodka

Industry/Entity Type

Product

Logo Text

742 Vodka

Font styles to use
Other font styles liked:
• French Script MT

Colors
ec1f27
3176b5

Requirements
Must have
• Incorporate the name 742 Vodka
• Incorporate the 4 art designs as attached
• Font type is provided as an example
• 742 = French Script MT
• Vodka = Footlight MT light
Nice to have
• N/A
Should not have
• N/A

```html
<!DOCTYPE html>
<html lang="en">
<head>
<meta charset="utf-8">
<title>742 Vodka – Label Colourways</title>
<link rel="stylesheet" href="https://fonts.googleapis.com/css2?family=Libre+Baskerville:wght@700&family=Open+Sans:wght@600;700&display=swap">
<style>
  :root {
    --brand-red: #ec1f27;
    --brand-blue: #3176b5;
    --deep-blue: #1d4f96;
    --sky-blue: #5ab4e6;
    --white: #ffffff;
    --backdrop: #e4e8ea;
    --backdrop-shade: #c9d0d3;
  }
  * { margin: 0; padding: 0; box-sizing: border-box; }
  html, body {
    width: 1200px;
    height: 900px;
    overflow: hidden;
  }
  body {
    background: linear-gradient(180deg, var(--backdrop) 0%, var(--backdrop-shade) 100%);
    font-family: "Open Sans", Arial, sans-serif;
  }
  .label-sheet {
    position: relative;
    width: 1200px;
    height: 900px;
    display: flex;
    justify-content: center;
    align-items: center;
    gap: 60px;
  }
  .label {
    width: 400px;
    height: 540px;
    display: flex;
    flex-direction: column;
    box-shadow: 0 6px 18px rgba(0, 0, 0, 0.18);
  }
  .label__band {
    height: 40px;
    display: flex;
    align-items: center;
    justify-content: center;
    color: var(--white);
    font-weight: 700;
    font-size: 17px;
  }
  .label__art {
    position: relative;
    flex: 1;
    display: flex;
    align-items: center;
    justify-content: center;
  }
  .label__pattern {
    position: absolute;
    inset: 0;
  }
  .label__name {
    position: relative;
    font-family: "Libre Baskerville", Georgia, serif;
    font-weight: 700;
    color: var(--white);
    text-align: center;
    line-height: 1.05;
  }
  .label__name-number {
    display: block;
    font-size: 120px;
  }
  .label__name-word {
    display: block;
    font-size: 52px;
    letter-spacing: 2px;
  }
  .label__info {
    height: 62px;
    padding: 6px 10px;
    color: var(--white);
    display: flex;
    flex-direction: column;
    justify-content: center;
  }
  .label__specs {
    display: flex;
    justify-content: space-between;
    font-size: 19px;
    font-weight: 600;
  }
  .label__origin {
    font-size: 13.5px;
    font-weight: 700;
    letter-spacing: 0.1px;
  }

  /* Colourway: blue band, red art */
  .label--red-art .label__band,
  .label--red-art .label__info {
    background: linear-gradient(90deg, var(--deep-blue) 0%, var(--brand-blue) 60%, var(--sky-blue) 100%);
  }
  .label--red-art .label__pattern {
    background:
      radial-gradient(circle at 30% 35%, rgba(49, 118, 181, 0.35) 0 18%, transparent 40%),
      radial-gradient(circle at 75% 70%, rgba(49, 118, 181, 0.3) 0 15%, transparent 38%),
      var(--brand-red);
  }

  /* Colourway: red band, blue art */
  .label--blue-art .label__band,
  .label--blue-art .label__info {
    background: var(--brand-red);
  }
  .label--blue-art .label__pattern {
    background:
      radial-gradient(circle at 30% 35%, rgba(236, 31, 39, 0.3) 0 16%, transparent 38%),
      radial-gradient(circle at 75% 70%, rgba(236, 31, 39, 0.25) 0 14%, transparent 36%),
      linear-gradient(135deg, var(--deep-blue) 0%, var(--brand-blue) 55%, var(--sky-blue) 100%);
  }
</style>
</head>
<body>
  <main class="label-sheet">
    <section class="label label--red-art">
      <div class="label__band">Distilled from Natural Spirits</div>
      <div class="label__art">
        <div class="label__pattern" role="img" aria-label="Ceremonial vèvè symbol pattern in blue on red"></div>
        <h1 class="label__name">
          <span class="label__name-number">742</span>
          <span class="label__name-word">VODKA</span>
        </h1>
      </div>
      <div class="label__info">
        <div class="label__specs"><span>43%VOL</span><span>750ml</span></div>
        <div class="label__origin">PRODUCED AND DISTILLED IN THE CARIBBEAN</div>
      </div>
    </section>

    <section class="label label--blue-art">
      <div class="label__band">Distilled from Natural Spirits</div>
      <div class="label__art">
        <div class="label__pattern" role="img" aria-label="Ceremonial vèvè symbol pattern in red on blue"></div>
        <h2 class="label__name">
          <span class="label__name-number">742</span>
          <span class="label__name-word">VODKA</span>
        </h2>
      </div>
      <div class="label__info">
        <div class="label__specs"><span>43%VOL</span><span>750ml</span></div>
        <div class="label__origin">PRODUCED AND DISTILLED IN THE CARIBBEAN</div>
      </div>
    </section>
  </main>
</body>
</html>
```